Corporate Hollowmere business cards to be handed to investor, bankers etc. Needs to have a young feel

I need business cards designed for a technology company that provides vanto-like rapid response on the security industry. I would like it simple but very cool and tasteful. See attached documents for artwork and colours to be used. Cut sheet describes business model. Card stock should be thicker than normal. I would like the one side to be just the art and the other to have the contact info with maybe the pin somewhere.

Target Market(s)

Investors

Industry/Entity Type

Business

Contact Information for Business Card

Would like the logo attached on one side with name address and other info on the other side.

Font styles to use
Other font styles liked:
• See existing logo

Colors
6b449b
886aae
e4daeb
ffffff

Requirements
Must have
• Name: Gregory Thalassides
• Address: 47 Orchard Lane, Toronto, On, L6R2C8
• Tel: 647-5550192
• Email: greg@hollowmere.io
Nice to have
• See logo colours

```html
<!DOCTYPE html>
<html lang="en">
<head>
<meta charset="utf-8">
<title>Hollowmere Business Cards</title>
<link rel="stylesheet" href="https://fonts.googleapis.com/css2?family=Source+Sans+3:wght@300;400;600&display=swap">
<style>
  :root {
    --backdrop: #3a322e;
    --card: #141416;
    --card-edge: #1d1d20;
    --brand-purple: #6b449b;
    --accent-purple: #886aae;
    --lilac: #e4daeb;
    --white: #ffffff;
    --silver: #9c9ca0;
    --divider: #d8d8dc;
  }
  * { margin: 0; padding: 0; box-sizing: border-box; }
  html, body {
    width: 1200px;
    height: 864px;
    overflow: hidden;
    background: var(--backdrop);
    font-family: "Source Sans 3", sans-serif;
  }
  .stage {
    position: relative;
    width: 1200px;
    height: 864px;
  }
  .card {
    position: absolute;
    width: 530px;
    height: 303px;
    background: var(--card);
    border: 1px solid var(--card-edge);
    border-radius: 3px;
    box-shadow: 0 18px 40px rgba(0,0,0,0.45);
  }
  /* Front: brand side */
  .card-front {
    left: 50px;
    top: 220px;
  }
  .brand {
    position: absolute;
    left: 70px;
    top: 88px;
    display: flex;
    align-items: center;
    gap: 12px;
  }
  .brand-dot {
    width: 28px;
    height: 28px;
    border-radius: 50%;
    background: var(--silver);
  }
  .brand-name {
    font-size: 62px;
    font-weight: 300;
    letter-spacing: 1px;
    color: var(--silver);
    line-height: 1;
    text-transform: lowercase;
  }
  .brand-url {
    position: absolute;
    left: 72px;
    top: 212px;
    font-size: 13px;
    letter-spacing: 5px;
    color: var(--silver);
  }
  /* Back: contact side */
  .card-back {
    left: 620px;
    top: 340px;
  }
  .mark-circle {
    position: absolute;
    left: 58px;
    top: 92px;
    width: 118px;
    height: 118px;
    border-radius: 50%;
    background: var(--accent-purple);
  }
  .divider {
    position: absolute;
    left: 222px;
    top: 78px;
    width: 1px;
    height: 148px;
    background: linear-gradient(to bottom, transparent, var(--divider) 20%, var(--divider) 80%, transparent);
  }
  .contact {
    position: absolute;
    left: 244px;
    top: 84px;
    color: var(--white);
    font-size: 16px;
    line-height: 22px;
  }
  .contact-name {
    color: var(--accent-purple);
    font-weight: 600;
    font-size: 16px;
    letter-spacing: 0.5px;
    text-transform: uppercase;
    margin-bottom: 4px;
  }
  .contact-row {
    display: flex;
    align-items: center;
    gap: 8px;
  }
  .contact-icon {
    width: 13px;
    height: 13px;
    flex: none;
  }
</style>
</head>
<body>
<main class="stage">
  <section class="card card-front" aria-label="Card front">
    <div class="brand">
      <span class="brand-dot"></span>
      <span class="brand-name">Hollowmere</span>
    </div>
    <div class="brand-url">www.hollowmere.io</div>
  </section>

  <section class="card card-back" aria-label="Card back">
    <div class="mark-circle"></div>
    <div class="divider"></div>
    <div class="contact">
      <div class="contact-name">Gregory Thalassides</div>
      <div class="contact-line">47 Orchard Lane</div>
      <div class="contact-line">Toronto, On, L6R2C8</div>
      <div class="contact-row">
        <svg class="contact-icon" viewBox="0 0 16 16" aria-hidden="true">
          <path fill="#886aae" d="M1 5c0-2 2-3 7-3s7 1 7 3v1h-4V5H5v1H1zM3 7h10l1 7H2zM8 9a2 2 0 1 0 0 4a2 2 0 0 0 0-4z"/>
        </svg>
        <span>647-5550192</span>
      </div>
      <div class="contact-row">
        <svg class="contact-icon" viewBox="0 0 16 16" aria-hidden="true">
          <rect x="1" y="3" width="14" height="10" rx="1" fill="#886aae"/>
          <path d="M1.5 3.5 8 9l6.5-5.5" fill="none" stroke="#141416" stroke-width="1.3"/>
        </svg>
        <span>greg@hollowmere.io</span>
      </div>
      <div class="contact-row">
        <svg class="contact-icon" viewBox="0 0 16 16" aria-hidden="true">
          <circle cx="8" cy="8" r="7" fill="#886aae"/>
          <path d="M1 8h14M8 1c-3 3-3 11 0 14M8 1c3 3 3 11 0 14" fill="none" stroke="#141416" stroke-width="1"/>
        </svg>
        <span>www.hollowmere.io</span>
      </div>
    </div>
  </section>
</main>
</body>
</html>
```